Can you create a Business Card based on the Logo you designed.

See example and would like to see other examples.

Trying to keep it very clean with a focus on the logo and name.

```html
<!DOCTYPE html>
<html lang="en">
<head>
<meta charset="utf-8">
<title>Verdanta — Business Card</title>
<link rel="stylesheet" href="https://fonts.googleapis.com/css2?family=Open+Sans:wght@400;600;700&display=swap">
<style>
  :root {
    --stage: #222224;
    --paper: #ffffff;
    --card-dark: #1c1c1f;
    --mark-dark: #2e2e33;
    --green-deep: #0f7a45;
    --green-fresh: #7cc242;
    --orange: #f29b38;
    --ink: #1a1a1a;
  }
  * { margin: 0; padding: 0; box-sizing: border-box; }
  html, body {
    width: 1200px; height: 780px; overflow: hidden;
    background: var(--stage);
    font-family: "Open Sans", Arial, sans-serif;
  }
  .canvas { position: relative; width: 1200px; height: 780px; }

  .card {
    position: absolute; top: 247px;
    width: 500px; height: 286px;
    border-radius: 2px;
  }
  .card--front { left: 70px; background: var(--paper); }
  .card--back { left: 630px; background: var(--card-dark); }

  .brand {
    position: absolute;
    display: flex; align-items: center; gap: 8px;
    font-weight: 700; letter-spacing: -0.5px; line-height: 1;
  }
  .brand__dot { border-radius: 50%; background: var(--orange); flex: none; }
  .card--front .brand { left: 175px; top: 42px; font-size: 44px; color: var(--green-deep); }
  .card--front .brand__dot { width: 20px; height: 20px; }
  .card--back .brand { left: 50%; top: 50%; transform: translate(-50%, -50%); font-size: 60px; color: var(--mark-dark); }
  .card--back .brand__dot { width: 26px; height: 26px; }

  .holder { position: absolute; left: 150px; top: 118px; }
  .holder__name { font-size: 25px; font-weight: 700; line-height: 1.1; color: var(--green-fresh); }
  .holder__name .surname { color: var(--orange); }
  .holder__title { font-size: 13px; font-weight: 400; color: var(--ink); margin-top: 2px; }

  .contact-rule {
    position: absolute; left: 40px; right: 28px; top: 200px;
    height: 1.5px; background: var(--green-fresh);
  }
  .contact-icon {
    position: absolute; top: 189px;
    width: 23px; height: 23px; border-radius: 50%;
    background: var(--paper); border: 1.5px solid var(--green-fresh);
    display: flex; align-items: center; justify-content: center;
  }
  .contact-icon svg { width: 12px; height: 12px; }
  .contact-icon--phone { left: 70px; }
  .contact-icon--mail { left: 225px; }
  .contact-icon--web { left: 412px; }

  .contact-text {
    position: absolute; top: 228px;
    font-size: 12px; color: var(--ink); letter-spacing: 0.2px;
  }
  .contact-text--phone { left: 30px; }
  .contact-text--mail { left: 178px; }
  .contact-text--web { left: 345px; }
</style>
</head>
<body>
<main class="canvas">

  <section class="card card--front" aria-label="Business card front">
    <div class="brand"><span class="brand__name">Verdanta</span><span class="brand__dot"></span></div>

    <div class="holder">
      <p class="holder__name">Marcus <span class="surname">Hale</span></p>
      <p class="holder__title">Chief Executive Officer</p>
    </div>

    <div class="contact-rule"></div>

    <span class="contact-icon contact-icon--phone">
      <svg viewBox="0 0 24 24" aria-hidden="true"><path fill="var(--orange)" d="M6.6 10.8a15 15 0 0 0 6.6 6.6l2.2-2.2a1 1 0 0 1 1-.25 11.4 11.4 0 0 0 3.6.57 1 1 0 0 1 1 1V20a1 1 0 0 1-1 1A17 17 0 0 1 3 4a1 1 0 0 1 1-1h3.5a1 1 0 0 1 1 1c0 1.25.2 2.45.57 3.57a1 1 0 0 1-.25 1z"/></svg>
    </span>
    <span class="contact-icon contact-icon--mail">
      <svg viewBox="0 0 24 24" aria-hidden="true"><rect x="2" y="5" width="20" height="14" rx="2" fill="var(--orange)"/><path d="M3 6l9 7 9-7" fill="none" stroke="#fff" stroke-width="1.8"/></svg>
    </span>
    <span class="contact-icon contact-icon--web">
      <svg viewBox="0 0 24 24" aria-hidden="true"><circle cx="12" cy="12" r="10" fill="var(--orange)"/><path d="M2 12h20M12 2c3 3 3 17 0 20M12 2c-3 3-3 17 0 20" fill="none" stroke="#fff" stroke-width="1.4"/></svg>
    </span>

    <span class="contact-text contact-text--phone">+1 (555) 014-2290</span>
    <span class="contact-text contact-text--mail">ceo@verdanta.com</span>
    <span class="contact-text contact-text--web">www.verdanta.com</span>
  </section>

  <section class="card card--back" aria-label="Business card back">
    <div class="brand"><span class="brand__name">Verdanta</span><span class="brand__dot"></span></div>
  </section>

</main>
</body>
</html>
```